Dune Air & Plus business card

I need an awesome, double-sided business card designed with our new logo. I would like the one side black with the colored logo, and the back side is all yours. I'd like to see horizontal and vertical layouts. Get creative! Thank you.

Target Market(s)

HVAC, Heating and Cooling in Phoenix, AZ

Industry/Entity Type

HVAC

Contact Information for Business Card

We need our new logo on the card. Tom Harker, (623) 555-0142, tom@trydunesair.com, www.trydunesair.com, ROC 514273

```html
<!DOCTYPE html>
<html lang="en">
<head>
<meta charset="utf-8">
<title>Dune Air &amp; Plus — Business Card</title>
<link href="https://fonts.googleapis.com/css2?family=Poppins:wght@400;500;600;800&display=swap" rel="stylesheet">
<style>
  :root {
    --navy: #06203c;
    --card: #050505;
    --card-edge: #0d0d0d;
    --white: #ffffff;
    --brand-orange: #f2811d;
    --brand-blue: #1a7fd6;
  }
  * { margin: 0; padding: 0; box-sizing: border-box; }
  html, body {
    width: 1051px; height: 1200px; overflow: hidden;
    background: var(--navy);
    font-family: "Poppins", sans-serif;
    color: var(--white);
  }
  .canvas { position: relative; width: 1051px; height: 1200px; }
  .card {
    position: absolute; left: 105px; width: 841px; height: 480px;
    border-radius: 36px; overflow: hidden;
    background: radial-gradient(ellipse at center, var(--card-edge) 0%, var(--card) 80%);
    box-shadow: 0 6px 18px rgba(0,0,0,.45);
  }
  .card-front { top: 81px; }
  .card-back { top: 639px; }

  .brand-mark {
    position: absolute; left: 50%; top: 50%;
    transform: translate(-50%, -50%);
    display: flex; align-items: center; gap: 16px;
  }
  .brand-dot {
    width: 30px; height: 30px; border-radius: 50%;
    background: var(--brand-orange);
  }
  .brand-name {
    font-weight: 800; font-size: 46px; letter-spacing: .5px;
    color: var(--brand-orange); white-space: nowrap;
  }

  .person { position: absolute; left: 64px; top: 178px; }
  .person-name {
    font-weight: 800; font-size: 70px; line-height: 1; letter-spacing: -1.5px;
  }
  .person-title {
    font-weight: 400; font-size: 29px; line-height: 1; margin-top: 14px;
  }

  .divider {
    position: absolute; left: 501px; top: 79px;
    width: 2px; height: 324px; background: var(--white);
  }
  .contact-list { position: absolute; left: 517px; top: 79px; list-style: none; }
  .contact-item {
    display: flex; align-items: center; gap: 12px;
    height: 47px; margin-bottom: 45px;
  }
  .contact-icon {
    width: 47px; height: 47px; border-radius: 50%;
    background: var(--white);
    display: flex; align-items: center; justify-content: center;
    flex: none;
  }
  .contact-icon svg { width: 26px; height: 26px; }
  .contact-label { font-weight: 600; font-size: 16.5px; line-height: 1.15; }
  .contact-value { font-weight: 400; font-size: 18px; line-height: 1.15; letter-spacing: .3px; }
</style>
</head>
<body>
<main class="canvas">

  <section class="card card-front" role="img" aria-label="Black card face with a faint repeating brand pattern and the Dune Air & Plus name">
    <div class="brand-mark">
      <span class="brand-dot"></span>
      <span class="brand-name">Dune Air &amp; Plus</span>
    </div>
  </section>

  <section class="card card-back" role="img" aria-label="Black card back with a faint repeating brand pattern and contact details">
    <div class="person">
      <h1 class="person-name">Tom Harker</h1>
      <p class="person-title">General Manager</p>
    </div>

    <div class="divider"></div>

    <ul class="contact-list">
      <li class="contact-item">
        <span class="contact-icon">
          <svg viewBox="0 0 24 24"><path d="M12 2a7 7 0 0 0-7 7c0 5 7 13 7 13s7-8 7-13a7 7 0 0 0-7-7zm0 9.5A2.5 2.5 0 1 1 12 6.5a2.5 2.5 0 0 1 0 5z" fill="#050505"/></svg>
        </span>
        <div>
          <p class="contact-label">Visit Us here</p>
          <p class="contact-value">ROC 514273</p>
        </div>
      </li>
      <li class="contact-item">
        <span class="contact-icon">
          <svg viewBox="0 0 24 24" fill="none" stroke="#050505" stroke-width="1.2"><circle cx="12" cy="12" r="9.5"/><ellipse cx="12" cy="12" rx="4.5" ry="9.5"/><line x1="2.5" y1="12" x2="21.5" y2="12"/><line x1="12" y1="2.5" x2="12" y2="21.5"/><path d="M4.5 7h15M4.5 17h15"/></svg>
        </span>
        <div>
          <p class="contact-label">Visit Our Website</p>
          <p class="contact-value">www.trydunesair.com</p>
        </div>
      </li>
      <li class="contact-item">
        <span class="contact-icon">
          <svg viewBox="0 0 24 24" fill="none" stroke="#050505" stroke-width="1.6"><rect x="3" y="5.5" width="18" height="13" rx="2.5"/><path d="M3.5 7l8.5 6 8.5-6"/></svg>
        </span>
        <div>
          <p class="contact-label">Email Address</p>
          <p class="contact-value">tom@trydunesair.com</p>
        </div>
      </li>
      <li class="contact-item">
        <span class="contact-icon">
          <svg viewBox="0 0 24 24"><path d="M6.6 10.8a15.1 15.1 0 0 0 6.6 6.6l2.2-2.2a1 1 0 0 1 1-.25 11.4 11.4 0 0 0 3.6.57 1 1 0 0 1 1 1V20a1 1 0 0 1-1 1A17 17 0 0 1 3 4a1 1 0 0 1 1-1h3.5a1 1 0 0 1 1 1c0 1.25.2 2.45.57 3.6a1 1 0 0 1-.25 1z" fill="#050505"/></svg>
        </span>
        <div>
          <p class="contact-label">Office Number</p>
          <p class="contact-value">(623) 555-0142</p>
        </div>
      </li>
    </ul>
  </section>

</main>
</body>
</html>
```